Disability and mental health support work company requires business card

Specialising
Wrenfield Disability is a new QCAP service aimed toward QCAP participants with a history of criminal justice, psychosocial/mental health, intellectual, and cognitive disabilities.

Our focus
Focusing on providing core QCAP supports for community participation, daily activities and supported independent living.

Authentic
Likeminded people wanting to make a difference in participant's lives.

Our aim to provide holistic and empowering supports targeted towards creating independence and guidance for all participants and families.
Over 35 years of experience working with people that have psychosocial, intellectual, and cognitive disabilities.

Industry/Entity Type

disability and mental health

Contact Information for Business Card

logo - business name

Colors
0054AA
0677BA
7BADD7
CADEEF
E8F1F8
FFF300
FFF600
FEFA6F
FFFEC7
FFFEE8

Requirements
Must have
• want double sided business cards(wont let me change it)
Should not have
• any disability related pictures

```html
<!DOCTYPE html>
<html lang="en">
<head>
<meta charset="UTF-8">
<title>Wrenfield Disability – Business Card</title>
<link href="https://fonts.googleapis.com/css2?family=Montserrat:wght@400;500;700;800&display=swap" rel="stylesheet">
<style>
  :root {
    --canvas-bg: #e6e7e9;
    --navy: #13365d;
    --sky: #7aadde;
    --card-white: #ffffff;
    --ink: #2b2b2b;
  }
  html, body {
    margin: 0;
    padding: 0;
    width: 1048px;
    height: 1200px;
    overflow: hidden;
    background: var(--canvas-bg);
    font-family: "Montserrat", Arial, sans-serif;
  }
  .canvas {
    position: relative;
    width: 1048px;
    height: 1200px;
  }
  .card {
    position: absolute;
    width: 843px;
    height: 482px;
    box-shadow: 0 10px 28px rgba(0, 0, 0, 0.22);
    overflow: hidden;
  }
  .card--front {
    left: 84px;
    top: 87px;
    background: var(--card-white);
  }
  .card--back {
    left: 77px;
    top: 623px;
    background: var(--navy);
  }
  .person-name {
    position: absolute;
    left: 38px;
    top: 62px;
    margin: 0;
    font-size: 35px;
    font-weight: 800;
    letter-spacing: -1px;
    color: var(--navy);
    line-height: 1;
  }
  .person-role {
    position: absolute;
    left: 37px;
    top: 106px;
    margin: 0;
    font-size: 23px;
    font-weight: 400;
    letter-spacing: 0.5px;
    color: var(--ink);
  }
  .contact-list {
    position: absolute;
    left: 46px;
    top: 296px;
    margin: 0;
    padding: 0;
    list-style: none;
    font-size: 21px;
    color: var(--ink);
  }
  .contact-list li {
    display: flex;
    align-items: center;
    height: 30px;
  }
  .contact-list svg {
    width: 20px;
    height: 20px;
    margin-right: 13px;
    fill: var(--navy);
  }
  .address {
    position: absolute;
    left: 45px;
    top: 398px;
    margin: 0;
    font-style: normal;
    font-size: 22px;
    line-height: 32px;
    color: var(--ink);
    letter-spacing: 0.3px;
  }
  .brand-disc {
    position: absolute;
    border-radius: 50%;
    background: var(--navy);
    display: flex;
    align-items: center;
    justify-content: center;
  }
  .card--front .brand-disc {
    left: 367px;
    top: 7px;
    width: 470px;
    height: 470px;
    box-shadow: 0 0 0 2px var(--sky);
  }
  .card--back .brand-disc {
    left: 238px;
    top: 57px;
    width: 366px;
    height: 366px;
    border: 1.5px solid var(--sky);
    box-sizing: border-box;
    box-shadow: 0 6px 18px rgba(0, 0, 0, 0.3);
  }
  .brand-name {
    margin: 0;
    text-align: center;
    font-weight: 700;
    color: var(--sky);
    line-height: 1.15;
  }
  .card--front .brand-name { font-size: 38px; }
  .card--back .brand-name { font-size: 30px; }
</style>
</head>
<body>
<div class="canvas">

  <section class="card card--front" aria-label="Business card front">
    <h1 class="person-name">DANIEL HARTLEY</h1>
    <p class="person-role">Managing Director</p>

    <ul class="contact-list">
      <li>
        <svg viewBox="0 0 24 24" aria-hidden="true"><path d="M6.6 10.8a15.1 15.1 0 0 0 6.6 6.6l2.2-2.2c.3-.3.7-.4 1-.2 1.1.4 2.3.6 3.6.6.6 0 1 .4 1 1V20c0 .6-.4 1-1 1A17 17 0 0 1 3 4c0-.6.4-1 1-1h3.5c.6 0 1 .4 1 1 0 1.3.2 2.5.6 3.6.1.3 0 .7-.2 1z"/></svg>
        044-987 210 346
      </li>
      <li>
        <svg viewBox="0 0 24 24" aria-hidden="true"><path d="M2 5h20v14H2z M4 7v.4l8 5.3 8-5.3V7z" fill-rule="evenodd"/></svg>
        hello@wrenfield.com
      </li>
      <li>
        <svg viewBox="0 0 24 24" aria-hidden="true"><path d="M12 2a10 10 0 1 0 0 20 10 10 0 0 0 0-20zm-1 17.9A8 8 0 0 1 4.2 10L9 14.8v1a2 2 0 0 0 2 2zm6.9-2.5A2 2 0 0 0 16 16h-1v-3a1 1 0 0 0-1-1H8v-2h2a1 1 0 0 0 1-1V7h2a2 2 0 0 0 2-2v-.4a8 8 0 0 1 2.9 12.8z"/></svg>
        www.wrenfieldcare.com
      </li>
    </ul>

    <address class="address">58, Harbour Lane<br>Northvale, 40218</address>

    <div class="brand-disc">
      <p class="brand-name">Wrenfield<br>Disability</p>
    </div>
  </section>

  <section class="card card--back" aria-label="Business card back">
    <div class="brand-disc">
      <p class="brand-name">Wrenfield<br>Disability</p>
    </div>
  </section>

</div>
</body>
</html>
```